We sincerely appreciate everyone's interest in our website design project. In all we had 65 designs submitted and were amazed by the creativity and quality presented. Unfortunately, as with all contests, there can only be one winner and the winning firm was selected at 12:00 ET 7/7/2017. We wish you all the best and look forward to potentially working with you on future projects. Thanks again for your time and interests. Tobin

Thanks for your interest in our project! Due to the overwhelming number of submissions received, additional submissions will not be accepted after close of business 7/4. Additionally, to minimize unnecessary additional work, we will begin reviewing all submissions received on 7/5, select the submission(s) that come closest to meeting our needs and work with the designer(s) selected to finalize their designs. Thanks again.

Thanks for the feedback!!

Based on feedback provided, we understand that the initial specifications required that the site be developed as dynamic versus static and, as such, the budget was insufficient. With this in mind, we have modified the specifications as follows:
1. Clean, simple, uncluttered site
2. 4-5 pages consisting of the following:
a. Home page
b. About us
c. Services provided
d. Contact us/request quote/request service
2. No people in pools/photos unless it involves cleaning i.e., vacuuming, netting, etc.

We are in need of a website to promote our business and the services provided to our customers. The site should be a simple 5 page design providing information about us, the services we provide, our service territory (Central Florida = Seminole and Orange Counties), the ability to request a service quote, the ability to schedule service, the ability to pay invoices, the ability to refer neighbors and friends, the ability to leave reviews and provide feedback, etc. We are a certified, licensed, and insured veteran minority owned and operated company with 10 years industry experience providing unparalleled commercial and residential pool and spa care in the central Florida area. While we are seeking something more impressive and concise, an example of the site would be http://marlowpoolservice.example/ OR http://www.bluefinchpoolcompany.example/

Target Market(s)

Hotels, motels, apartment complexes, condominium associations, homeowners associations, and individual homeowners

Industry/Entity Type

It Company

Contact Information for Business Card

Logo, name, phone number, website, "Certified Licensed Insured", "Providing quality pool care to Central Florida"

Coding

Coded - Design and coding required

Number of Pages Required

5+ page

Requirements
Must have
• See description
Nice to have
• See description
Should not have
• See description

```html
<!DOCTYPE html>
<html lang="en">
<head>
<meta charset="utf-8">
<title>Sunward Pool Care</title>
<link rel="stylesheet" href="https://fonts.googleapis.com/css2?family=Raleway:ital,wght@0,400;0,500;0,600;0,700;0,800;1,400&display=swap">
<style>
:root{
  --blue:#1f5fa3;
  --blue-dark:#174d87;
  --orange:#d9622a;
  --orange-dark:#c2521f;
  --text:#444;
  --gray:#f0f0f0;
  --footer:#2f2f2f;
  --white:#fff;
}
*{box-sizing:border-box;margin:0;padding:0}
html,body{width:1200px;height:2866px;overflow:hidden}
body{position:relative;font-family:'Raleway',sans-serif;color:var(--text);background:var(--white)}
.abs{position:absolute}
.btn{position:absolute;display:flex;align-items:center;justify-content:center;background:linear-gradient(var(--orange),var(--orange-dark));color:#fff;font-weight:700;font-size:13px;letter-spacing:.5px;text-transform:uppercase;border-radius:2px}
.heading{color:var(--blue);font-weight:700;font-size:27px;letter-spacing:.3px;text-transform:uppercase}
.para{font-size:14.5px;line-height:23px;color:var(--text)}

/* header */
.header{left:0;top:0;width:1200px;height:122px;border-top:4px solid var(--blue);background:#fff}
.brand{left:75px;top:44px;font-weight:800;font-size:31px;color:var(--blue);line-height:1;white-space:nowrap}
.phone-tab{left:873px;top:0;width:251px;height:48px;background:var(--blue);color:#fff;font-weight:700;font-size:19px;display:flex;align-items:center;justify-content:center;gap:12px;clip-path:polygon(0 0,100% 0,96% 100%,4% 100%)}
.nav{left:449px;top:69px;display:flex;font-size:13px;font-weight:600;color:#222;text-transform:uppercase}
.nav a{display:flex;align-items:center;height:42px;padding:0 14px}
.nav a.active{background:linear-gradient(var(--orange),var(--orange-dark));color:#fff;padding:0 17px;margin-right:6px}

/* hero */
.hero{left:0;top:122px;width:1200px;height:539px;background:linear-gradient(160deg,#5f7f4a 0%,#9bbf8a 12%,#2fa7d6 30%,#1e96cf 60%,#c9b8a3 80%,#d8cbb9 100%)}
.hero-tag{left:75px;background:rgba(9,46,66,.82);color:#fff;font-weight:700;text-transform:uppercase;letter-spacing:.5px}
.tag1{top:285px;height:55px;padding:0 22px;font-size:31px;display:flex;align-items:center}
.tag2{top:348px;width:602px;padding:10px 22px;font-size:31px;line-height:44px}
.dots{left:75px;top:601px;display:flex;gap:12px}
.dots span{width:11px;height:11px;border-radius:50%;background:#222}
.dots span.on{background:var(--orange)}
.quote{left:793px;top:183px;width:334px;height:417px;background:#fff;box-shadow:0 3px 12px rgba(0,0,0,.3)}
.quote h2{height:60px;background:linear-gradient(var(--blue),var(--blue-dark));color:#fff;font-size:23px;font-weight:700;padding:0 20px;display:flex;align-items:center}
.field{position:absolute;left:23px;width:288px;height:42px;border:1px solid #d4d4d4;border-radius:2px;font-size:12.5px;color:#555;padding:13px 14px}
.quote .btn{left:23px;top:357px;width:288px;height:48px;font-size:14px}

/* welcome */
.welcome{left:76px;top:705px;width:1048px;text-align:center}
.welcome .para{margin-top:20px;font-size:15px;line-height:23px}

/* services */
.svc{left:0;width:1200px;height:374px;overflow:hidden}
.svc .photo{position:absolute;inset:0}
.svc svg{position:absolute;left:0;top:0}
.svc-copy{position:absolute;width:490px}
.svc-copy .para{margin-top:18px}
.svc-copy .btn{position:relative;margin-top:32px;width:150px;height:45px}

/* video + testimonials */
.video{left:75px;top:2209px;width:512px;height:283px;background:linear-gradient(180deg,#2a4750 0%,#3b6b7a 45%,#6a5a4a 75%,#8a7560 100%)}
.play{position:absolute;left:217px;top:111px;width:78px;height:55px;border-radius:10px;background:#fff;display:flex;align-items:center;justify-content:center}
.testi{left:612px;width:515px}
.testi .mark{position:absolute;left:0;top:0;color:var(--orange);font-size:110px;font-weight:800;line-height:.8;font-family:Georgia,serif}
.testi p{margin-left:114px;font-style:italic;font-size:14px;line-height:23px;color:#444}
.testi .who{margin-left:114px;margin-top:12px;color:var(--orange);font-weight:700;font-size:13px}

/* footer */
.footer{left:0;top:2570px;width:1200px;height:296px;background:var(--footer);border-top:7px solid var(--blue);color:#ddd}
.fcol{position:absolute;top:54px;font-size:13px;line-height:28px}
.fcol h3{color:var(--orange);font-size:14px;font-weight:700;text-transform:uppercase;margin-bottom:4px}
.fcol .row{display:flex;gap:18px;align-items:center}
.map{left:564px;top:56px;width:286px;height:183px;background:linear-gradient(135deg,#e6e2d5,#cfdcc2 50%,#e9e3d2)}
.fbrand{left:898px;top:72px;font-weight:800;font-size:28px;color:#bbb;line-height:1;white-space:nowrap}
.copy{left:898px;top:148px;font-size:12.5px;line-height:22px;color:#bbb}
.social{left:898px;top:220px;display:flex;gap:22px}
.social span{width:18px;height:18px;border-radius:50%;background:#fff}
</style>
</head>
<body>

<header class="abs header">
  <div class="abs brand">Sunward Pool Care</div>
  <div class="abs phone-tab">
    <svg width="18" height="18" viewBox="0 0 24 24"><path fill="#fff" d="M6.6 10.8a15 15 0 006.6 6.6l2.2-2.2c.3-.3.7-.4 1-.2 1.1.4 2.3.6 3.6.6.6 0 1 .4 1 1V20c0 .6-.4 1-1 1A17 17 0 013 4c0-.6.4-1 1-1h3.5c.6 0 1 .4 1 1 0 1.3.2 2.5.6 3.6.1.3 0 .7-.2 1z"/></svg>
    1-800-555-0142
  </div>
  <nav class="abs nav">
    <a class="active">Home</a><a>About Us</a><a>Services</a><a>Request Quote</a><a>Request Service</a><a>Contact Us</a>
  </nav>
</header>

<section class="abs hero" role="img" aria-label="Photo of a clear blue swimming pool with a steel ladder and paved deck"></section>
<div class="abs hero-tag tag1">Sunward Pool Care</div>
<div class="abs hero-tag tag2">We are a swimming pool care services company</div>
<div class="abs dots"><span class="on"></span><span></span><span></span><span></span></div>

<form class="abs quote">
  <h2>REQUEST QUOTE</h2>
  <div class="field" style="top:83px">Name</div>
  <div class="field" style="top:134px">Email Address</div>
  <div class="field" style="top:185px">Phone No.</div>
  <div class="field" style="top:236px">Subject<svg style="position:absolute;right:14px;top:17px" width="9" height="6" viewBox="0 0 9 6"><path d="M1 1l3.5 3.5L8 1" stroke="#555" fill="none" stroke-width="1.4"/></svg></div>
  <div class="field" style="top:287px;height:58px">Message</div>
  <div class="btn">Submit</div>
</form>

<section class="abs welcome">
  <h1 class="heading">Welcome to our website</h1>
  <p class="para">Aliquam molestie, mi et imperdiet euismod, dui purus auctor tellus, et interdum lacus lectus et ante. Sed accumsan sollicitudin sapien, sit amet adipiscing turpis gravida ac. In congue, neque ac lobortis volutpat, libero mauris varius mi, vitae suscipit ipsum ligula vitae risus. Duis aliquam nibh a dui iaculis viverra id a velit. Vivamus egestas risus in magna varius commodo. Sed semper viverra egestas. Etiam pretium porttitor lectus, vel ornare neque porta volutpat.</p>
</section>
<div class="btn" style="left:525px;top:879px;width:151px;height:46px">Read More</div>

<section class="abs svc" style="top:984px">
  <div class="photo" role="img" aria-label="Photo of a tiled pool with an under maintenance chalkboard sign" style="background:linear-gradient(135deg,#6ccbe0,#2f9fc4 50%,#8fa9b0)"></div>
  <svg width="1200" height="374"><path d="M675 0 C560 60 470 200 449 374 L1200 374 L1200 0Z" fill="var(--gray)"/></svg>
  <div class="svc-copy" style="left:636px;top:75px">
    <h2 class="heading">Pool Service &amp; Maintenance</h2>
    <p class="para">Aliquam molestie, mi et imperdiet euismod, dui purus auctor tellus, et interdum lacus lectus et ante. Sed accumsan sollicitudin sapien, sit amet adipiscing turpis gravida ac. In congue, neque ac lobortis volutpat, libero mauris varius mi...</p>
    <div class="btn">Read More</div>
  </div>
</section>

<section class="abs svc" style="top:1357px">
  <div class="photo" role="img" aria-label="Photo of pool renovation work with fresh concrete and brick edging" style="background:linear-gradient(135deg,#55585a,#7c7670 50%,#a7958a)"></div>
  <svg width="1200" height="374"><path d="M0 0 L525 0 C660 60 720 170 690 260 C670 320 640 350 625 374 L0 374Z" fill="#fff"/></svg>
  <div class="svc-copy" style="left:75px;top:75px">
    <h2 class="heading">Pool Repair &amp; Renovations</h2>
    <p class="para">Aliquam molestie, mi et imperdiet euismod, dui purus auctor tellus, et interdum lacus lectus et ante. Sed accumsan sollicitudin sapien, sit amet adipiscing turpis gravida ac. In congue, neque ac lobortis volutpat, libero mauris varius mi...</p>
    <div class="btn">Read More</div>
  </div>
</section>

<section class="abs svc" style="top:1731px">
  <div class="photo" role="img" aria-label="Photo of a rooftop commercial pool with city towers behind" style="background:linear-gradient(180deg,#8a8f94 0%,#a99e8f 35%,#3e6e94 65%,#2a5f8e 100%)"></div>
  <svg width="1200" height="375"><path d="M670 0 C560 50 500 200 508 375 L1200 375 L1200 0Z" fill="var(--gray)"/></svg>
  <div class="svc-copy" style="left:636px;top:75px">
    <h2 class="heading">Commercial Pool Services</h2>
    <p class="para">Aliquam molestie, mi et imperdiet euismod, dui purus auctor tellus, et interdum lacus lectus et ante. Sed accumsan sollicitudin sapien, sit amet adipiscing turpis gravida ac. In congue, neque ac lobortis volutpat, libero mauris varius mi...</p>
    <div class="btn">Read More</div>
  </div>
</section>

<h2 class="abs heading" style="left:75px;top:2152px">Watch a video</h2>
<div class="abs video" role="img" aria-label="Video still of an automatic pool vacuum cleaning a pool">
  <div class="play"><svg width="24" height="26" viewBox="0 0 24 26"><path d="M2 1l21 12L2 25z" fill="#2a4750"/></svg></div>
</div>

<h2 class="abs heading" style="left:614px;top:2152px">Testimonials</h2>
<div class="abs testi" style="top:2208px">
  <div class="mark">&ldquo;</div>
  <p>&ldquo;&nbsp; Aliquam molestie, mi et imperdiet euismod, dui purus auctor tellus, et interdum lacus lectus et ante accumsan sollicitudin sapien, sit amet adipiscing turpis gravida ac. In congue, neque ac lobortis.&rdquo;</p>
  <div class="who">-NAME HEADING</div>
</div>
<div class="abs" style="left:612px;top:2350px;width:515px;height:1px;background:#ddd"></div>
<div class="abs testi" style="top:2376px">
  <div class="mark">&ldquo;</div>
  <p>&ldquo;&nbsp; Aliquam molestie, mi et imperdiet euismod, dui purus auctor tellus, et interdum lacus lectus et ante accumsan sollicitudin sapien, sit amet adipiscing turpis gravida ac. In congue, neque ac lobortis.&rdquo;</p>
  <div class="who">-NAME HEADING</div>
</div>

<footer class="abs footer">
  <div class="fcol" style="left:75px">
    <h3>Site Map</h3>
    Home<br>About us<br>Services<br>Request Quote<br>Request Service<br>Contact us
  </div>
  <div class="fcol" style="left:319px">
    <h3>Contact Info</h3>
    412 Heron Lane<br>Orlando, FL 32801
    <div class="row"><svg width="12" height="12" viewBox="0 0 24 24"><path fill="#ddd" d="M6.6 10.8a15 15 0 006.6 6.6l2.2-2.2c.3-.3.7-.4 1-.2 1.1.4 2.3.6 3.6.6.6 0 1 .4 1 1V20c0 .6-.4 1-1 1A17 17 0 013 4c0-.6.4-1 1-1h3.5c.6 0 1 .4 1 1 0 1.3.2 2.5.6 3.6.1.3 0 .7-.2 1z"/></svg>1-800-555-0142</div>
    <div class="row"><svg width="12" height="10" viewBox="0 0 12 10"><rect width="12" height="10" fill="#ddd"/><path d="M0 0l6 5 6-5" stroke="#2f2f2f" fill="none"/></svg>info@sunwardpool.example</div>
    <div class="row"><svg width="12" height="10" viewBox="0 0 12 10"><rect width="12" height="10" fill="#ddd"/><path d="M0 0l6 5 6-5" stroke="#2f2f2f" fill="none"/></svg>Map Direction</div>
  </div>
  <div class="abs map" role="img" aria-label="Street map of the service area"></div>
  <div class="abs fbrand">Sunward Pool Care</div>
  <div class="abs copy">Copyright &copy; 2017. Company Name<br>All Right Reserved.</div>
  <div class="abs social" aria-label="Social links"><span></span><span></span><span></span><span></span><span></span></div>
</footer>

</body>
</html>
```